Powerpoint Presentation (urgent)

We need a powerpoint presentation to accompany our other pitch materials for a really exciting, new project.

It is a project related to gaming.

The presentation should be engaging, professionally done, and be trendy and captivating.

```html
<!DOCTYPE html>
<html lang="en">
<head>
<meta charset="utf-8">
<title>Gaming Pitch Deck – Slide Overview</title>
<link href="https://fonts.googleapis.com/css2?family=Montserrat:ital,wght@0,300;0,400;0,500;0,600;0,700;1,400&display=swap" rel="stylesheet">
<style>
:root{
  --canvas:#b5b5b5;
  --ink:#1b1b1b;
  --ink-2:#2b2b2b;
  --mid:#555;
  --muted:#8a8a8a;
  --faint:#bdbdbd;
  --paper:#ffffff;
  --red:#c8162b;
  --purple:#5e2a8e;
  --green:#1c8f3f;
  --blue:#2b4f9f;
  --grey-box:#7a7a7a;
}
*{box-sizing:border-box;margin:0;padding:0}
html,body{width:1200px;height:1200px;overflow:hidden;background:var(--canvas);font-family:'Montserrat',sans-serif}
.deck{position:absolute;left:100px;top:46px;display:grid;grid-template-columns:repeat(4,230px);grid-template-rows:repeat(6,173px);column-gap:15.5px;row-gap:15.2px}
.slide{position:relative;width:230px;height:173px;background:var(--paper);overflow:hidden}
.head{position:absolute;left:0;top:0;width:100%;height:37px;background:linear-gradient(115deg,#121212 0%,#2e2e2e 28%,#161616 46%,#292929 70%,#111 100%)}
.head h2{position:absolute;left:16px;top:25px;font-size:6.2px;font-weight:700;color:#fff;letter-spacing:.1px}
.foot{position:absolute;left:0;bottom:0;width:100%;height:13px;background:linear-gradient(100deg,#151515,#262626 50%,#151515)}
.foot span{position:absolute;left:16px;top:5px;font-size:2.6px;color:#555}
.a{position:absolute}
.t{font-size:2.3px;line-height:3px;color:var(--muted)}
.h{font-size:2.6px;font-weight:700;color:var(--ink);text-transform:uppercase;margin-bottom:1.4px}
.w{color:#fff}
.i{width:100%;height:100%;fill:none;stroke:currentColor;stroke-width:2;stroke-linecap:round;stroke-linejoin:round}
.dot{position:absolute;border-radius:50%;display:flex;align-items:center;justify-content:center}
.photo{position:absolute}
.ph-keys{background:linear-gradient(160deg,#4a5a3a,#1d2618 60%,#0d120b)}
.ph-pad{background:radial-gradient(circle at 50% 60%,#4aa3e0,#134b8a 55%,#0a2444)}
.ph-player{background:linear-gradient(140deg,#0e1a33,#2a3f6e 45%,#8a2232 80%,#1a1a1a)}
.ph-dark{background:linear-gradient(150deg,#1a2233,#0c0f16 50%,#2b1414 80%,#0b0b0b)}
.avatar{position:absolute;width:28px;height:28px;border-radius:50%;background:radial-gradient(circle at 45% 40%,#9a8a80,#4d4a4a 70%,#2b2b2b)}
</style>
</head>
<body>
<svg width="0" height="0" style="position:absolute">
  <symbol id="cloud" viewBox="0 0 24 24"><path d="M7 18a5 5 0 0 1-.5-10 6 6 0 0 1 11.5 2 4 4 0 0 1 0 8M12 11v8m-3-3 3 3 3-3"/></symbol>
  <symbol id="doc" viewBox="0 0 24 24"><path d="M6 3h8l4 4v14H6zM14 3v4h4M9 12h6M9 16h6"/></symbol>
  <symbol id="bell" viewBox="0 0 24 24"><path d="M5 17h14l-2-3v-4a5 5 0 0 0-10 0v4zM10 20h4"/></symbol>
  <symbol id="chat" viewBox="0 0 24 24"><path d="M3 5h18v11H9l-4 4v-4H3zM8 10.5h.01M12 10.5h.01M16 10.5h.01"/></symbol>
  <symbol id="bulb" viewBox="0 0 24 24"><path d="M9 18h6M10 21h4M12 3a6 6 0 0 0-4 10.5c1 1 1 2 1 3h6c0-1 0-2 1-3A6 6 0 0 0 12 3z"/></symbol>
  <symbol id="mail" viewBox="0 0 24 24"><path d="M3 6h18v12H3zM3 6l9 7 9-7"/></symbol>
  <symbol id="phone" viewBox="0 0 24 24"><path d="M8 2h8v20H8zM11 18h2"/></symbol>
  <symbol id="mouse" viewBox="0 0 24 24"><path d="M7 9a5 5 0 0 1 10 0v6a5 5 0 0 1-10 0zM12 4v5"/></symbol>
  <symbol id="batt" viewBox="0 0 24 24"><path d="M3 8h16v8H3zM21 11v2M6 10.5v3M9 10.5v3M12 10.5v3M15 10.5v3"/></symbol>
  <symbol id="wifi" viewBox="0 0 24 24"><path d="M2 9a15 15 0 0 1 20 0M5 12.5a10 10 0 0 1 14 0M8.5 16a5 5 0 0 1 7 0M12 19.5h.01"/></symbol>
  <symbol id="send" viewBox="0 0 24 24"><path d="M21 3 3 11l7 2 2 7zM10 13 21 3"/></symbol>
  <symbol id="clock" viewBox="0 0 24 24"><circle cx="12" cy="12" r="9"/><path d="M12 7v5l3 2"/></symbol>
  <symbol id="pen" viewBox="0 0 24 24"><path d="M4 20l1-5L16 4l4 4L9 19zM14 6l4 4"/></symbol>
  <symbol id="bag" viewBox="0 0 24 24"><path d="M3 8h18v12H3zM9 8V5h6v3M3 13h18"/></symbol>
  <symbol id="camera" viewBox="0 0 24 24"><path d="M3 8h4l2-3h6l2 3h4v11H3z"/><circle cx="12" cy="13" r="3.5"/></symbol>
  <symbol id="lock" viewBox="0 0 24 24"><path d="M5 11h14v10H5zM8 11V7a4 4 0 0 1 8 0v4"/></symbol>
  <symbol id="call" viewBox="0 0 24 24"><path d="M5 3h4l2 5-3 2a11 11 0 0 0 6 6l2-3 5 2v4a2 2 0 0 1-2 2A17 17 0 0 1 3 5a2 2 0 0 1 2-2z"/></symbol>
  <symbol id="globe" viewBox="0 0 24 24"><circle cx="12" cy="12" r="9"/><path d="M3 12h18M12 3a14 14 0 0 1 0 18M12 3a14 14 0 0 0 0 18"/></symbol>
</svg>

<main class="deck">

  <!-- 1 Title -->
  <section class="slide" style="background:linear-gradient(125deg,#0f0f0f,#2a2a2a 30%,#141414 52%,#262626 75%,#0e0e0e)">
    <div class="a" style="left:91px;top:96px;font-size:15px;font-weight:300;line-height:20px;color:#7a7a7a">Presentation<br>Title Goes Here</div>
    <div class="a" style="left:95px;top:138px;font-size:3.6px;color:#555">www.questline.io</div>
  </section>

  <!-- 2 Numbered points -->
  <section class="slide">
    <div class="head"><h2>HEADING GOES HERE</h2></div>
    <div class="dot" style="left:15px;top:58px;width:7px;height:7px;background:var(--ink);font-size:2.8px;color:#fff;font-weight:700">1</div>
    <div class="a" style="left:27px;top:58px;width:50px"><div class="h" style="font-size:2.2px">Lorem ipsum dolor</div><div class="t" style="font-size:1.9px;line-height:2.5px">Lorem ipsum dolor sit amet consectetur adipiscing elit sed do eiusmod tempor incididunt ut labore</div></div>
    <div class="dot" style="left:15px;top:88px;width:7px;height:7px;background:var(--ink);font-size:2.8px;color:#fff;font-weight:700">2</div>
    <div class="a" style="left:27px;top:88px;width:50px"><div class="h" style="font-size:2.2px">Lorem ipsum dolor</div><div class="t" style="font-size:1.9px;line-height:2.5px">Lorem ipsum dolor sit amet consectetur adipiscing elit sed do eiusmod tempor incididunt ut labore</div></div>
    <div class="dot" style="left:15px;top:118px;width:7px;height:7px;background:var(--ink);font-size:2.8px;color:#fff;font-weight:700">3</div>
    <div class="a" style="left:27px;top:118px;width:50px"><div class="h" style="font-size:2.2px">Lorem ipsum dolor</div><div class="t" style="font-size:1.9px;line-height:2.5px">Lorem ipsum dolor sit amet consectetur adipiscing elit sed do eiusmod tempor incididunt ut labore</div></div>
    <div class="dot" style="left:80px;top:58px;width:7px;height:7px;background:var(--ink);font-size:2.8px;color:#fff;font-weight:700">4</div>
    <div class="a" style="left:92px;top:58px;width:50px"><div class="h" style="font-size:2.2px">Lorem ipsum dolor</div><div class="t" style="font-size:1.9px;line-height:2.5px">Lorem ipsum dolor sit amet consectetur adipiscing elit sed do eiusmod tempor incididunt ut labore</div></div>
    <div class="dot" style="left:80px;top:88px;width:7px;height:7px;background:var(--ink);font-size:2.8px;color:#fff;font-weight:700">5</div>
    <div class="a" style="left:92px;top:88px;width:50px"><div class="h" style="font-size:2.2px">Lorem ipsum dolor</div><div class="t" style="font-size:1.9px;line-height:2.5px">Lorem ipsum dolor sit amet consectetur adipiscing elit sed do eiusmod tempor incididunt ut labore</div></div>
    <div class="dot" style="left:80px;top:118px;width:7px;height:7px;background:var(--ink);font-size:2.8px;color:#fff;font-weight:700">6</div>
    <div class="a" style="left:92px;top:118px;width:50px"><div class="h" style="font-size:2.2px">Lorem ipsum dolor</div><div class="t" style="font-size:1.9px;line-height:2.5px">Lorem ipsum dolor sit amet consectetur adipiscing elit sed do eiusmod tempor incididunt ut labore</div></div>
    <div class="a" style="left:149px;top:59px;width:72px"><div class="h" style="font-size:2.6px">Sed ut perspiciatis unde</div><div class="t" style="font-size:2.4px;line-height:3.1px;color:#666">Iste natus error sit voluptatem accusantium doloremque laudantium, totam rem aperiam, eaque ipsa quae ab illo inventore veritatis et quasi architecto beatae vitae dicta sunt explicabo. Nemo enim ipsam voluptatem quia voluptas sit aspernatur aut odit aut fugit, sed quia consequuntur magni dolores eos qui ratione voluptatem sequi nesciunt. Neque porro quisquam est, qui dolorem ipsum quia dolor sit amet, consectetur, adipisci velit, commodi consequatur.</div></div>
    <div class="foot"><span>www.questline.io</span></div>
  </section>

  <!-- 3 Rings -->
  <section class="slide">
    <div class="head"><h2>HEADING GOES HERE</h2></div>
    <svg class="a" style="left:0;top:37px" width="230" height="80" viewBox="0 0 230 80">
      <g fill="none" stroke-width="6">
        <circle cx="41" cy="43" r="24" stroke="var(--red)"/>
        <circle cx="90" cy="43" r="24" stroke="#333"/>
        <circle cx="140" cy="43" r="24" stroke="var(--purple)"/>
        <circle cx="190" cy="43" r="24" stroke="var(--green)"/>
      </g>
      <g font-family="Montserrat,sans-serif" font-size="2.2" font-weight="700" text-anchor="middle">
        <text x="41" y="52" fill="var(--red)">LOREM IPSUM</text>
        <text x="90" y="52" fill="#333">LOREM IPSUM</text>
        <text x="140" y="52" fill="var(--purple)">LOREM IPSUM</text>
        <text x="190" y="52" fill="var(--green)">LOREM IPSUM</text>
      </g>
      <g class="i" style="stroke-width:1.6">
        <use href="#cloud" x="35" y="32" width="12" height="12" stroke="var(--red)"/>
        <use href="#doc" x="84" y="32" width="12" height="12" stroke="#333"/>
        <use href="#bell" x="134" y="32" width="12" height="12" stroke="var(--purple)"/>
        <use href="#chat" x="184" y="32" width="12" height="12" stroke="var(--green)"/>
      </g>
    </svg>
    <div class="a t" style="left:16px;top:124px;width:198px;text-align:center;font-size:2.2px;line-height:2.9px">Iste natus error sit voluptatem accusantium doloremque laudantium, totam rem aperiam, eaque ipsa quae ab illo inventore veritatis et quasi architecto beatae vitae dicta sunt explicabo. Nemo enim ipsam voluptatem quia voluptas sit aspernatur aut odit aut fugit, sed quia consequuntur magni dolores eos qui ratione voluptatem sequi nesciunt. Neque porro quisquam est, qui dolorem ipsum quia dolor sit amet.</div>
    <div class="foot"><span>www.questline.io</span></div>
  </section>

  <!-- 4 Text columns -->
  <section class="slide">
    <div class="head"><h2>HEADING GOES HERE</h2></div>
    <div class="a t" style="left:16px;top:62px;width:85px;font-size:2.8px;line-height:3.6px;color:#555">Lorem ipsum dolor sit amet, consectetur adipiscing elit, sed do eiusmod tempor incididunt ut labore et dolore magna aliqua. Ut enim ad minim veniam, quis nostrud exercitation ullamco laboris nisi ut aliquip ex ea commodo consequat.<br><br>Duis aute irure dolor in reprehenderit in voluptate velit esse cillum dolore eu fugiat nulla pariatur. Excepteur sint occaecat cupidatat non proident, sunt in culpa qui officia deserunt mollit anim id est laborum.</div>
    <div class="a" style="left:124px;top:62px;width:92px;font-size:4.4px;line-height:5.4px;font-style:italic;color:#333">Itaque earum rerum hic tenetur a sapiente delectus, ut aut reiciendis voluptatibus maiores alias consequatur aut perferendis doloribus asperiores repellat.</div>
    <div class="foot"><span>www.questline.io</span></div>
  </section>

  <!-- 5 Icon line -->
  <section class="slide">
    <div class="head"><h2>HEADING GOES HERE</h2></div>
    <div class="a" style="left:0;top:85.5px;width:230px;height:.6px;background:#cfcfcf"></div>
    <div class="dot" style="left:36px;top:79px;width:14px;height:14px;border:1px solid var(--ink);background:#fff;color:var(--ink)"><svg class="i" style="width:8px;height:8px"><use href="#bulb"/></svg></div>
    <div class="dot" style="left:108px;top:79px;width:14px;height:14px;border:1px solid var(--ink);background:#fff;color:var(--ink)"><svg class="i" style="width:8px;height:8px"><use href="#mail"/></svg></div>
    <div class="dot" style="left:180px;top:79px;width:14px;height:14px;border:1px solid var(--ink);background:#fff;color:var(--ink)"><svg class="i" style="width:8px;height:8px"><use href="#phone"/></svg></div>
    <div class="a" style="left:20px;top:97px;width:46px;text-align:center"><div class="h" style="font-size:2.2px">Lorem ipsum dolor</div><div class="t" style="font-size:1.9px;line-height:2.5px">Lorem ipsum dolor sit amet, consectetur adipiscing elit, sed do eiusmod tempor incididunt ut labore et dolore</div></div>
    <div class="a" style="left:92px;top:97px;width:46px;text-align:center"><div class="h" style="font-size:2.2px">Lorem ipsum dolor</div><div class="t" style="font-size:1.9px;line-height:2.5px">Lorem ipsum dolor sit amet, consectetur adipiscing elit, sed do eiusmod tempor incididunt ut labore et dolore</div></div>
    <div class="a" style="left:164px;top:97px;width:46px;text-align:center"><div class="h" style="font-size:2.2px">Lorem ipsum dolor</div><div class="t" style="font-size:1.9px;line-height:2.5px">Lorem ipsum dolor sit amet, consectetur adipiscing elit, sed do eiusmod tempor incididunt ut labore et dolore</div></div>
    <div class="foot"><span>www.questline.io</span></div>
  </section>

  <!-- 6 Numbered blocks -->
  <section class="slide">
    <div class="head"><h2>HEADING GOES HERE</h2></div>
    <div class="a" style="left:10px;top:55px;font-size:24px;font-weight:300;color:#e2e2e2">01</div>
    <div class="a" style="left:49px;top:60px;width:58px"><div class="h" style="font-size:2.5px">Lorem ipsum dolor</div><div class="t">Lorem ipsum dolor sit amet, consectetur adipiscing elit, sed do eiusmod tempor incididunt ut labore et dolore magna aliqua</div></div>
    <div class="a" style="left:120px;top:55px;font-size:24px;font-weight:300;color:#e2e2e2">02</div>
    <div class="a" style="left:160px;top:60px;width:58px"><div class="h" style="font-size:2.5px">Lorem ipsum dolor</div><div class="t">Lorem ipsum dolor sit amet, consectetur adipiscing elit, sed do eiusmod tempor incididunt ut labore et dolore magna aliqua</div></div>
    <div class="a" style="left:10px;top:98px;font-size:24px;font-weight:300;color:#e2e2e2">03</div>
    <div class="a" style="left:49px;top:103px;width:58px"><div class="h" style="font-size:2.5px">Lorem ipsum dolor</div><div class="t">Lorem ipsum dolor sit amet, consectetur adipiscing elit, sed do eiusmod tempor incididunt ut labore et dolore magna aliqua</div></div>
    <div class="a" style="left:120px;top:98px;font-size:24px;font-weight:300;color:#e2e2e2">04</div>
    <div class="a" style="left:160px;top:103px;width:58px"><div class="h" style="font-size:2.5px">Lorem ipsum dolor</div><div class="t">Lorem ipsum dolor sit amet, consectetur adipiscing elit, sed do eiusmod tempor incididunt ut labore et dolore magna aliqua</div></div>
    <div class="foot"><span>www.questline.io</span></div>
  </section>

  <!-- 7 Team -->
  <section class="slide">
    <div class="head"><h2>HEADING GOES HERE</h2></div>
    <div class="a" style="left:115px;top:52px;width:.6px;height:96px;background:#e2e2e2"></div>
    <div class="a" style="left:16px;top:91px;width:198px;height:.6px;background:#e2e2e2"></div>
    <div class="avatar" role="img" aria-label="Team member portrait" style="left:19px;top:52px"></div>
    <div class="a" style="left:54px;top:58px;width:50px"><div style="font-size:4.2px;color:#222">Josh Doe</div><div class="h" style="font-size:1.9px">Executive Director</div><div class="t" style="font-size:1.9px;line-height:2.5px">Lorem ipsum dolor sit amet consectetur adipiscing elit sed do eiusmod tempor</div></div>
    <div class="avatar" role="img" aria-label="Team member portrait" style="left:128px;top:52px"></div>
    <div class="a" style="left:163px;top:58px;width:50px"><div style="font-size:4.2px;color:#222">Josh Doe</div><div class="h" style="font-size:1.9px">Executive Director</div><div class="t" style="font-size:1.9px;line-height:2.5px">Lorem ipsum dolor sit amet consectetur adipiscing elit sed do eiusmod tempor</div></div>
    <div class="avatar" role="img" aria-label="Team member portrait" style="left:19px;top:104px"></div>
    <div class="a" style="left:54px;top:110px;width:50px"><div style="font-size:4.2px;color:#222">Josh Doe</div><div class="h" style="font-size:1.9px">Executive Director</div><div class="t" style="font-size:1.9px;line-height:2.5px">Lorem ipsum dolor sit amet consectetur adipiscing elit sed do eiusmod tempor</div></div>
    <div class="avatar" role="img" aria-label="Team member portrait" style="left:128px;top:104px"></div>
    <div class="a" style="left:163px;top:110px;width:50px"><div style="font-size:4.2px;color:#222">Josh Doe</div><div class="h" style="font-size:1.9px">Executive Director</div><div class="t" style="font-size:1.9px;line-height:2.5px">Lorem ipsum dolor sit amet consectetur adipiscing elit sed do eiusmod tempor</div></div>
    <div class="foot"><span>www.questline.io</span></div>
  </section>

  <!-- 8 Three photos -->
  <section class="slide">
    <div class="head"><h2>HEADING GOES HERE</h2></div>
    <div class="photo ph-keys" role="img" aria-label="Photo of a backlit gaming keyboard" style="left:10px;top:62px;width:66px;height:34px"></div>
    <div class="photo ph-pad" role="img" aria-label="Photo of a game controller in blue light" style="left:82px;top:62px;width:66px;height:34px"></div>
    <div class="photo ph-player" role="img" aria-label="Photo of a player at an esports event" style="left:154px;top:62px;width:66px;height:34px"></div>
    <div class="a" style="left:10px;top:100px;width:64px"><div class="h" style="font-size:2.4px">Lorem ipsum dolor</div><div class="t" style="font-size:1.9px;line-height:2.5px">Lorem ipsum dolor sit amet, consectetur adipiscing elit, sed do eiusmod tempor incididunt ut labore et dolore magna aliqua</div></div>
    <div class="a" style="left:82px;top:100px;width:64px"><div class="h" style="font-size:2.4px">Lorem ipsum dolor</div><div class="t" style="font-size:1.9px;line-height:2.5px">Lorem ipsum dolor sit amet, consectetur adipiscing elit, sed do eiusmod tempor incididunt ut labore et dolore magna aliqua</div></div>
    <div class="a" style="left:154px;top:100px;width:64px"><div class="h" style="font-size:2.4px">Lorem ipsum dolor</div><div class="t" style="font-size:1.9px;line-height:2.5px">Lorem ipsum dolor sit amet, consectetur adipiscing elit, sed do eiusmod tempor incididunt ut labore et dolore magna aliqua</div></div>
    <div class="foot"><span>www.questline.io</span></div>
  </section>

  <!-- 9 Colour grid -->
  <section class="slide">
    <div class="head"><h2>HEADING GOES HERE</h2></div>
    <div class="photo ph-keys" role="img" aria-label="Photo of a gaming keyboard" style="left:16px;top:54px;width:66px;height:44px"></div>
    <div class="a" style="left:82px;top:54px;width:67px;height:44px;background:var(--purple);padding:9px 4px"><div class="h w" style="font-size:2.4px">Lorem ipsum dolor</div><div class="t" style="font-size:1.9px;line-height:2.5px;color:#d6c6ea">Lorem ipsum dolor sit amet, consectetur adipiscing elit, sed do eiusmod tempor incididunt ut labore et dolore magna</div></div>
    <div class="photo ph-player" role="img" aria-label="Photo of a player with headset" style="left:149px;top:54px;width:66px;height:44px"></div>
    <div class="a" style="left:16px;top:98px;width:66px;height:44px;background:var(--red);padding:10px 5px"><div class="h w" style="font-size:2.4px">Lorem ipsum dolor</div><div class="t" style="font-size:1.9px;line-height:2.5px;color:#f3c5cb">Lorem ipsum dolor sit amet, consectetur adipiscing elit, sed do eiusmod tempor incididunt ut labore et dolore magna</div></div>
    <div class="photo ph-pad" role="img" aria-label="Photo of a game controller" style="left:82px;top:98px;width:67px;height:44px"></div>
    <div class="a" style="left:149px;top:98px;width:66px;height:44px;background:var(--green);padding:10px 4px"><div class="h w" style="font-size:2.4px">Lorem ipsum dolor</div><div class="t" style="font-size:1.9px;line-height:2.5px;color:#c6ecd2">Lorem ipsum dolor sit amet, consectetur adipiscing elit, sed do eiusmod tempor incididunt ut labore et dolore magna</div></div>
    <div class="foot"><span>www.questline.io</span></div>
  </section>

  <!-- 10 Three icon columns -->
  <section class="slide">
    <div class="head"><h2>HEADING GOES HERE</h2></div>
    <div class="a" style="left:90px;top:62px;width:.6px;height:68px;background:#e0e0e0"></div>
    <div class="a" style="left:152px;top:62px;width:.6px;height:68px;background:#e0e0e0"></div>
    <svg class="i a" style="left:34px;top:63px;width:10px;height:10px;color:#222"><use href="#mouse"/></svg>
    <svg class="i a" style="left:104px;top:63px;width:12px;height:10px;color:#222"><use href="#batt"/></svg>
    <svg class="i a" style="left:175px;top:63px;width:12px;height:10px;color:#222"><use href="#wifi"/></svg>
    <div class="a" style="left:14px;top:79px;width:66px;text-align:center"><div class="h" style="font-size:2.6px">Lorem ipsum dolor</div><div class="t">Lorem ipsum dolor sit amet, consectetur adipiscing elit, sed do eiusmod tempor incididunt ut labore et dolore magna aliqua. Ut enim ad minim veniam, quis nostrud exercitation</div></div>
    <div class="a" style="left:89px;top:79px;width:64px;text-align:center"><div class="h" style="font-size:2.6px">Lorem ipsum dolor</div><div class="t">Lorem ipsum dolor sit amet, consectetur adipiscing elit, sed do eiusmod tempor incididunt ut labore et dolore magna aliqua. Ut enim ad minim veniam, quis nostrud exercitation</div></div>
    <div class="a" style="left:160px;top:79px;width:64px;text-align:center"><div class="h" style="font-size:2.6px">Lorem ipsum dolor</div><div class="t">Lorem ipsum dolor sit amet, consectetur adipiscing elit, sed do eiusmod tempor incididunt ut labore et dolore magna aliqua. Ut enim ad minim veniam, quis nostrud exercitation</div></div>
    <div class="foot"><span>www.questline.io</span></div>
  </section>

  <!-- 11 Devices -->
  <section class="slide">
    <div class="head"><h2>HEADING GOES HERE</h2></div>
    <div class="photo" role="img" aria-label="Product mockup of monitor, laptop, tablet and phone" style="left:16px;top:60px;width:112px;height:56px;background:linear-gradient(180deg,#f4f4f4,#e6e6e6)"></div>
    <div class="a" style="left:150px;top:54px;width:72px"><div class="h" style="font-size:2.6px">Sed ut perspiciatis unde</div><div class="t" style="color:#666">Iste natus error sit voluptatem accusantium doloremque laudantium, totam rem aperiam, eaque ipsa quae ab illo inventore veritatis et quasi architecto beatae vitae dicta sunt explicabo. Nemo enim ipsam voluptatem quia voluptas sit aspernatur aut odit aut fugit, sed quia consequuntur magni dolores eos qui ratione voluptatem sequi nesciunt. Neque porro quisquam est, qui dolorem ipsum quia dolor sit amet, consectetur, adipisci velit, commodi consequatur.</div></div>
    <div class="foot"><span>www.questline.io</span></div>
  </section>

  <!-- 12 Video -->
  <section class="slide">
    <div class="head"><h2>HEADING GOES HERE</h2></div>
    <div class="a" style="left:12px;top:56px;width:76px"><div class="h" style="font-size:2.6px">Sed ut perspiciatis unde</div><div class="t" style="color:#666">Iste natus error sit voluptatem accusantium doloremque laudantium, totam rem aperiam, eaque ipsa quae ab illo inventore veritatis et quasi architecto beatae vitae dicta sunt explicabo. Nemo enim ipsam voluptatem quia voluptas sit aspernatur aut odit aut fugit, sed quia consequuntur magni dolores eos qui ratione voluptatem sequi nesciunt. Neque porro quisquam est, qui dolorem ipsum quia dolor sit amet, consectetur, adipisci velit.</div></div>
    <div class="a" style="left:98px;top:49px;width:114px;height:78px;background:#1d1d1d;border-radius:2px;padding:3px 3px 10px">
      <div role="img" aria-label="Video preview" style="width:100%;height:100%;background:linear-gradient(120deg,#0f6e6a,#3a5d8a 50%,#b0344a)"></div>
    </div>
    <div class="a" style="left:98px;top:117px;width:114px;height:10px;background:#e6e6e6"></div>
    <div class="a" style="left:146px;top:127px;width:18px;height:10px;background:linear-gradient(#cfcfcf,#e6e6e6)"></div>
    <div class="a" style="left:140px;top:136px;width:30px;height:2px;background:#d4d4d4;border-radius:1px"></div>
    <div class="foot"><span>www.questline.io</span></div>
  </section>

  <!-- 13 Map -->
  <section class="slide">
    <div class="head"><h2>HEADING GOES HERE</h2></div>
    <div class="photo" role="img" aria-label="Dotted world map with location markers" style="left:28px;top:50px;width:176px;height:104px;background:radial-gradient(ellipse at 50% 45%,#dcdcdc,#eeeeee 65%,#fff 80%)"></div>
    <div class="foot"><span>www.questline.io</span></div>
  </section>

  <!-- 14 Coloured boxes -->
  <section class="slide">
    <div class="head"><h2>HEADING GOES HERE</h2></div>
    <div class="a t" style="left:14px;top:44px;width:202px;text-align:center;font-size:2.2px;line-height:2.9px">Iste natus error sit voluptatem accusantium doloremque laudantium, totam rem aperiam, eaque ipsa quae ab illo inventore veritatis et quasi architecto beatae vitae dicta sunt explicabo. Nemo enim ipsam voluptatem quia voluptas sit aspernatur aut odit aut fugit, sed quia consequuntur magni dolores eos qui ratione voluptatem sequi nesciunt.</div>
    <div class="a" style="left:13px;top:73px;width:55px;height:72px;background:var(--blue);padding:7px 5px;text-align:center">
      <div class="dot" style="position:relative;margin:0 auto 5px;width:11px;height:11px;border:.7px solid #fff;color:#fff"><svg class="i" style="width:6px;height:6px"><use href="#send"/></svg></div>
      <div class="h w" style="font-size:2.4px">Lorem ipsum dolor</div><div class="t" style="color:#cfd9f0">Lorem ipsum dolor sit amet, consectetur adipiscing elit, sed do eiusmod tempor incididunt ut labore et dolore magna aliqua</div></div>
    <div class="a" style="left:88px;top:73px;width:55px;height:72px;background:var(--grey-box);padding:7px 5px;text-align:center">
      <div class="dot" style="position:relative;margin:0 auto 5px;width:11px;height:11px;border:.7px solid #fff;color:#fff"><svg class="i" style="width:6px;height:6px"><use href="#clock"/></svg></div>
      <div class="h w" style="font-size:2.4px">Lorem ipsum dolor</div><div class="t" style="color:#e2e2e2">Lorem ipsum dolor sit amet, consectetur adipiscing elit, sed do eiusmod tempor incididunt ut labore et dolore magna aliqua</div></div>
    <div class="a" style="left:163px;top:73px;width:55px;height:72px;background:var(--red);padding:7px 5px;text-align:center">
      <div class="dot" style="position:relative;margin:0 auto 5px;width:11px;height:11px;border:.7px solid #fff;color:#fff"><svg class="i" style="width:6px;height:6px"><use href="#pen"/></svg></div>
      <div class="h w" style="font-size:2.4px">Lorem ipsum dolor</div><div class="t" style="color:#f3c5cb">Lorem ipsum dolor sit amet, consectetur adipiscing elit, sed do eiusmod tempor incididunt ut labore et dolore magna aliqua</div></div>
    <div class="foot"><span>www.questline.io</span></div>
  </section>

  <!-- 15 Pricing -->
  <section class="slide">
    <div class="head"><h2>HEADING GOES HERE</h2></div>
    <div class="a" style="left:14px;top:53px;width:60px;height:88px;background:#f0f0f0;text-align:center">
      <div style="background:var(--red);color:#fff;font-size:2.4px;font-weight:700;padding:2.5px 0">LOREM IPSUM DOLOR</div>
      <div style="font-size:2.6px;color:#444;margin-top:6px">30 DAYS FREE TRIAL</div>
      <div style="font-size:13px;color:#222;line-height:14px"><sup style="font-size:4px">$</sup>12<span style="font-size:6px">/mo</span></div>
      <div class="t" style="font-size:1.8px;line-height:4.6px;margin-top:3px">CONSECTETUR ADIPISCING ELIT<br>CONSECTETUR ADIPISCING ELIT<br>CONSECTETUR ADIPISCING ELIT<br>CONSECTETUR ADIPISCING ELIT</div>
      <div style="margin:3px auto 0;width:20px;font-size:1.8px;border:.4px solid #aaa;color:#666;padding:.6px 0">SELECT PLAN</div>
    </div>
    <div class="a" style="left:83px;top:44px;width:74px;height:107px;background:#ebebeb;text-align:center">
      <div style="background:var(--blue);color:#fff;font-size:2.8px;font-weight:700;padding:4px 0">LOREM IPSUM DOLOR</div>
      <div style="font-size:3px;color:#444;margin-top:7px">30 DAYS FREE TRIAL</div>
      <div style="font-size:16px;color:#222;line-height:18px"><sup style="font-size:5px">$</sup>12<span style="font-size:7.5px">/mo</span></div>
      <div class="t" style="font-size:2.1px;line-height:6px;margin-top:4px">CONSECTETUR ADIPISCING ELIT<br>CONSECTETUR ADIPISCING ELIT<br>CONSECTETUR ADIPISCING ELIT<br>CONSECTETUR ADIPISCING ELIT</div>
      <div style="margin:5px auto 0;width:24px;font-size:2px;border:.4px solid #aaa;color:#666;padding:.8px 0">SELECT PLAN</div>
    </div>
    <div class="a" style="left:166px;top:53px;width:60px;height:88px;background:#f0f0f0;text-align:center">
      <div style="background:var(--green);color:#fff;font-size:2.4px;font-weight:700;padding:2.5px 0">LOREM IPSUM DOLOR</div>
      <div style="font-size:2.6px;color:#444;margin-top:6px">30 DAYS FREE TRIAL</div>
      <div style="font-size:13px;color:#222;line-height:14px"><sup style="font-size:4px">$</sup>12<span style="font-size:6px">/mo</span></div>
      <div class="t" style="font-size:1.8px;line-height:4.6px;margin-top:3px">CONSECTETUR ADIPISCING ELIT<br>CONSECTETUR ADIPISCING ELIT<br>CONSECTETUR ADIPISCING ELIT<br>CONSECTETUR ADIPISCING ELIT</div>
      <div style="margin:3px auto 0;width:20px;font-size:1.8px;border:.4px solid #aaa;color:#666;padding:.6px 0">SELECT PLAN</div>
    </div>
    <div class="foot"><span>www.questline.io</span></div>
  </section>

  <!-- 16 Donut -->
  <section class="slide">
    <div class="head"><h2>HEADING GOES HERE</h2></div>
    <div class="dot" style="left:19px;top:62px;width:13px;height:13px;background:#555;color:#fff;font-size:3px">25%</div>
    <div class="a" style="left:39px;top:61px;width:72px"><div class="h" style="font-size:2.2px">Lorem ipsum dolor</div><div class="t" style="font-size:1.9px;line-height:2.5px">Lorem ipsum dolor sit amet, consectetur adipiscing elit, sed do eiusmod tempor incididunt ut labore et dolore magna aliqua</div></div>
    <div class="dot" style="left:19px;top:93px;width:13px;height:13px;background:#ddd;color:#fff;font-size:3px">50%</div>
    <div class="a" style="left:39px;top:92px;width:72px"><div class="h" style="font-size:2.2px">Lorem ipsum dolor</div><div class="t" style="font-size:1.9px;line-height:2.5px">Lorem ipsum dolor sit amet, consectetur adipiscing elit, sed do eiusmod tempor incididunt ut labore et dolore magna aliqua</div></div>
    <div class="dot" style="left:19px;top:124px;width:13px;height:13px;background:#555;color:#fff;font-size:3px">25%</div>
    <div class="a" style="left:39px;top:123px;width:72px"><div class="h" style="font-size:2.2px">Lorem ipsum dolor</div><div class="t" style="font-size:1.9px;line-height:2.5px">Lorem ipsum dolor sit amet, consectetur adipiscing elit, sed do eiusmod tempor incididunt ut labore et dolore magna aliqua</div></div>
    <svg class="a" style="left:126px;top:53px" width="92" height="92" viewBox="0 0 92 92">
      <path d="M46 46V1A45 45 0 0 1 46 91z" fill="#555"/>
      <path d="M46 46V91A45 45 0 0 1 1 46z" fill="#c4c4c4"/>
      <path d="M46 46H1A45 45 0 0 1 46 1z" fill="#1b1b1b"/>
      <g stroke="#fff" stroke-width="1.2"><line x1="46" y1="0" x2="46" y2="92"/><line x1="0" y1="46" x2="46" y2="46"/></g>
      <circle cx="46" cy="46" r="15" fill="#fff"/>
      <use href="#bag" x="40" y="40" width="12" height="12" fill="none" stroke="#222" stroke-width="2"/>
      <g font-family="Montserrat,sans-serif" font-size="5" fill="#fff"><text x="14" y="30">25%</text><text x="69" y="48">50%</text><text x="14" y="66">25%</text></g>
    </svg>
    <div class="foot"><span>www.questline.io</span></div>
  </section>

  <!-- 17 Bar chart -->
  <section class="slide">
    <div class="head"><h2>HEADING GOES HERE</h2></div>
    <svg class="a" style="left:16px;top:50px" width="124" height="96" viewBox="0 0 124 96">
      <g font-family="Montserrat,sans-serif" font-size="2.6" fill="#aaa"><text x="2" y="10">40</text><text x="2" y="30">30</text><text x="2" y="50">20</text><text x="2" y="70">10</text><text x="2" y="86">0</text></g>
      <line x1="10" y1="86" x2="122" y2="86" stroke="#ddd" stroke-width=".5"/>
      <rect x="18" y="49" width="5" height="37" fill="#1b1b1b"/><rect x="24" y="60" width="5" height="26" fill="#555"/><rect x="30" y="33" width="5" height="53" fill="#999"/>
      <rect x="56" y="65" width="5" height="21" fill="#1b1b1b"/><rect x="62" y="56" width="5" height="30" fill="#555"/><rect x="68" y="36" width="5" height="50" fill="#999"/>
      <rect x="94" y="49" width="5" height="37" fill="#1b1b1b"/><rect x="100" y="36" width="5" height="50" fill="#555"/><rect x="106" y="56" width="5" height="30" fill="#999"/>
      <g font-family="Montserrat,sans-serif" font-size="2.6" font-weight="700" fill="#444" text-anchor="middle"><text x="26" y="93">CATEGORY 1</text><text x="64" y="93">CATEGORY 2</text><text x="102" y="93">CATEGORY 3</text></g>
    </svg>
    <div class="dot" style="left:149px;top:58px;width:12px;height:12px;background:#1b1b1b;color:#fff"><svg class="i" style="width:6px;height:6px"><use href="#lock"/></svg></div>
    <div class="a" style="left:164px;top:58px;width:58px"><div class="h" style="font-size:2.2px">Lorem ipsum dolor</div><div class="t" style="font-size:1.9px;line-height:2.5px">Lorem ipsum dolor sit amet, consectetur adipiscing elit, sed do eiusmod tempor incididunt ut labore</div></div>
    <div class="dot" style="left:149px;top:83px;width:12px;height:12px;background:#555;color:#fff"><svg class="i" style="width:6px;height:6px"><use href="#camera"/></svg></div>
    <div class="a" style="left:164px;top:83px;width:58px"><div class="h" style="font-size:2.2px">Lorem ipsum dolor</div><div class="t" style="font-size:1.9px;line-height:2.5px">Lorem ipsum dolor sit amet, consectetur adipiscing elit, sed do eiusmod tempor incididunt ut labore</div></div>
    <div class="dot" style="left:149px;top:108px;width:12px;height:12px;background:#aaa;color:#fff"><svg class="i" style="width:6px;height:6px"><use href="#lock"/></svg></div>
    <div class="a" style="left:164px;top:108px;width:58px"><div class="h" style="font-size:2.2px">Lorem ipsum dolor</div><div class="t" style="font-size:1.9px;line-height:2.5px">Lorem ipsum dolor sit amet, consectetur adipiscing elit, sed do eiusmod tempor incididunt ut labore</div></div>
    <div class="foot"><span>www.questline.io</span></div>
  </section>

  <!-- 18 Timeline -->
  <section class="slide">
    <div class="head"><h2>HEADING GOES HERE</h2></div>
    <svg class="a" style="left:0;top:37px" width="230" height="123" viewBox="0 0 230 123">
      <line x1="0" y1="59" x2="230" y2="59" stroke="#e0e0e0" stroke-width=".6"/>
      <g fill="#222"><circle cx="36" cy="59" r="1"/><circle cx="88" cy="59" r="1"/><circle cx="140" cy="59" r="1"/><circle cx="186" cy="59" r="1"/></g>
      <g stroke="#e0e0e0" stroke-width=".5"><line x1="36" y1="41" x2="36" y2="58"/><line x1="140" y1="36" x2="140" y2="58"/><line x1="88" y1="60" x2="88" y2="80"/><line x1="186" y1="60" x2="186" y2="80"/></g>
      <circle cx="36" cy="29" r="13" fill="#1b1b1b"/><circle cx="140" cy="24" r="12" fill="#777"/>
      <circle cx="88" cy="92" r="13" fill="#333"/><circle cx="186" cy="92" r="13" fill="#aaa"/>
      <g fill="none" stroke="#fff" stroke-width="1.8" stroke-linecap="round" stroke-linejoin="round">
        <use href="#cloud" x="31" y="20" width="10" height="10"/><use href="#bell" x="135" y="15" width="10" height="10"/>
        <use href="#doc" x="83" y="83" width="10" height="10"/><use href="#chat" x="181" y="83" width="10" height="10"/>
      </g>
      <g font-family="Montserrat,sans-serif" font-size="1.9" font-weight="700" fill="#fff" text-anchor="middle">
        <text x="36" y="35">LOREM IPSUM</text><text x="140" y="30">LOREM IPSUM</text><text x="88" y="98">LOREM IPSUM</text><text x="186" y="98">LOREM IPSUM</text>
      </g>
      <g font-family="Montserrat,sans-serif" font-size="2" fill="#bbb" text-anchor="middle"><text x="36" y="65">2015</text><text x="88" y="65">2016</text><text x="140" y="65">2017</text><text x="186" y="65">2018</text></g>
    </svg>
    <div class="foot"><span>www.questline.io</span></div>
  </section>

  <!-- 19 Wave process -->
  <section class="slide">
    <div class="head"><h2>HEADING GOES HERE</h2></div>
    <svg class="a" style="left:0;top:37px" width="230" height="123" viewBox="0 0 230 123">
      <g fill="none" stroke-width="6">
        <path d="M14.5 53A19.5 19.5 0 0 1 53.5 53" stroke="#1b1b1b"/>
        <path d="M53.5 53A19.5 19.5 0 0 0 92.5 53" stroke="#777"/>
        <path d="M92.5 53A19.5 19.5 0 0 1 131.5 53" stroke="#1b1b1b"/>
        <path d="M131.5 53A19.5 19.5 0 0 0 170.5 53" stroke="#777"/>
        <path d="M170.5 53A19.5 19.5 0 0 1 209.5 53" stroke="#1b1b1b"/>
      </g>
      <g fill="#fff" stroke="#222" stroke-width=".6">
        <circle cx="34" cy="53" r="6"/><circle cx="73" cy="53" r="6" stroke="#777"/><circle cx="112" cy="53" r="6"/><circle cx="151" cy="53" r="6" stroke="#777"/><circle cx="190" cy="53" r="6"/>
      </g>
      <g fill="none" stroke="#222" stroke-width="2" stroke-linecap="round" stroke-linejoin="round">
        <use href="#bulb" x="30.5" y="49.5" width="7" height="7"/><use href="#mail" x="69.5" y="49.5" width="7" height="7" stroke="#777"/>
        <use href="#phone" x="108.5" y="49.5" width="7" height="7"/><use href="#batt" x="147.5" y="49.5" width="7" height="7" stroke="#777"/>
        <use href="#wifi" x="186.5" y="49.5" width="7" height="7"/>
      </g>
    </svg>
    <div class="a" style="left:16px;top:102px;width:36px;text-align:center"><div class="h" style="font-size:1.9px">Lorem ipsum dolor</div><div class="t" style="font-size:1.7px;line-height:2.3px">Lorem ipsum dolor sit amet consectetur adipiscing elit sed do eiusmod tempor</div></div>
    <div class="a" style="left:55px;top:65px;width:36px;text-align:center"><div class="h" style="font-size:1.9px">Lorem ipsum dolor</div><div class="t" style="font-size:1.7px;line-height:2.3px">Lorem ipsum dolor sit amet consectetur adipiscing elit sed do eiusmod tempor</div></div>
    <div class="a" style="left:94px;top:102px;width:36px;text-align:center"><div class="h" style="font-size:1.9px">Lorem ipsum dolor</div><div class="t" style="font-size:1.7px;line-height:2.3px">Lorem ipsum dolor sit amet consectetur adipiscing elit sed do eiusmod tempor</div></div>
    <div class="a" style="left:133px;top:65px;width:36px;text-align:center"><div class="h" style="font-size:1.9px">Lorem ipsum dolor</div><div class="t" style="font-size:1.7px;line-height:2.3px">Lorem ipsum dolor sit amet consectetur adipiscing elit sed do eiusmod tempor</div></div>
    <div class="a" style="left:172px;top:102px;width:36px;text-align:center"><div class="h" style="font-size:1.9px">Lorem ipsum dolor</div><div class="t" style="font-size:1.7px;line-height:2.3px">Lorem ipsum dolor sit amet consectetur adipiscing elit sed do eiusmod tempor</div></div>
    <div class="foot"><span>www.questline.io</span></div>
  </section>

  <!-- 20 Table -->
  <section class="slide">
    <div class="head"><h2>HEADING GOES HERE</h2></div>
    <div class="a" style="left:16px;top:52px;width:206px;height:86px;box-shadow:0 .5px 2px rgba(0,0,0,.15);display:grid;grid-template-columns:78px 58px 70px;grid-template-rows:17px 1fr;font-size:2.6px">
      <div style="background:#555;color:#fff;padding:7px 4px">CATEGORY</div>
      <div style="background:#9a9a9a;color:#fff;padding:7px 0;text-align:center;border-left:.6px solid #fff">COLUMN 1</div>
      <div style="background:#9a9a9a;color:#fff;padding:7px 0;text-align:center;border-left:.6px solid #fff">COLUMN 2</div>
      <div class="t" style="font-size:2px;line-height:8.8px;padding:2px 4px">SED UT PERSPICIATIS UNDE OMNIS<br>SED UT PERSPICIATIS UNDE OMNIS<br>SED UT PERSPICIATIS UNDE OMNIS<br>SED UT PERSPICIATIS UNDE OMNIS<br>SED UT PERSPICIATIS UNDE OMNIS</div>
      <div class="t" style="font-size:2px;line-height:8.8px;padding:2px 0;text-align:center;border-left:.6px solid #e5e5e5">VOLUPTATEM<br>VOLUPTATEM<br>VOLUPTATEM<br>VOLUPTATEM<br>VOLUPTATEM</div>
      <div class="t" style="font-size:2px;line-height:8.8px;padding:2px 0;text-align:center;border-left:.6px solid #e5e5e5">VOLUPTATEM<br>VOLUPTATEM<br>VOLUPTATEM<br>VOLUPTATEM<br>VOLUPTATEM</div>
    </div>
    <div class="foot"><span>www.questline.io</span></div>
  </section>

  <!-- 21 Chevrons -->
  <section class="slide">
    <div class="head"><h2>HEADING GOES HERE</h2></div>
    <svg class="a" style="left:16px;top:66px" width="204" height="62" viewBox="0 0 204 62">
      <polygon points="0,0 50,0 62,31 50,62 0,62 12,31" fill="#1b1b1b"/>
      <polygon points="48,0 98,0 110,31 98,62 48,62 60,31" fill="#333"/>
      <polygon points="96,0 146,0 158,31 146,62 96,62 108,31" fill="#555"/>
      <polygon points="144,0 192,0 204,31 192,62 144,62 156,31" fill="#a3a3a3"/>
    </svg>
    <div class="a w" style="left:40px;top:84px;font-size:4px;line-height:4.2px">Lorem<br>ipsum<br>dolor sit<br>amet, con-<br>sectetur</div>
    <div class="a w" style="left:88px;top:84px;font-size:4px;line-height:4.2px">Adipiscing<br>elit, sed do<br>eiusmod<br>tempor</div>
    <div class="a w" style="left:136px;top:84px;font-size:4px;line-height:4.2px">Ncididunt<br>ut labore<br>et dolore<br>magna<br>aliqua</div>
    <div class="a w" style="left:184px;top:84px;font-size:4px;line-height:4.2px">Excepteur<br>sint oc-<br>caecat<br>cupidatat<br>non pro-<br>dent</div>
    <div class="foot"><span>www.questline.io</span></div>
  </section>

  <!-- 22 Phone feature -->
  <section class="slide">
    <div class="photo ph-dark" role="img" aria-label="Photo of gamers at a tournament" style="left:0;top:0;width:230px;height:97px;opacity:.95"></div>
    <div class="a" style="left:18px;top:40px;width:28px;height:105px;background:#111;border-radius:4px;padding:9px 2px 12px"><div style="width:100%;height:100%;background:#fff"></div></div>
    <div class="a" style="left:100px;top:42px;width:120px;font-size:2.5px;line-height:3.2px;color:#e4e4e4">Iste natus error sit voluptatem accusantium doloremque laudantium, totam rem aperiam, eaque ipsa quae ab illo inventore veritatis et quasi architecto beatae vitae dicta sunt explicabo. Nemo enim ipsam voluptatem quia voluptas sit aspernatur aut odit aut fugit, sed quia consequuntur magni dolores eos qui ratione voluptatem sequi nesciunt. Neque porro quisquam est, qui dolorem ipsum quia dolor sit amet, consectetur, adipisci velit.</div>
    <div class="dot" style="left:98px;top:104px;width:8px;height:8px;border:.6px solid #222;color:#222"><svg class="i" style="width:4.5px;height:4.5px"><use href="#mail"/></svg></div>
    <div class="a" style="left:110px;top:104px;width:50px"><div class="h" style="font-size:2px">Lorem ipsum dolor</div><div class="t" style="font-size:1.8px;line-height:2.4px">Lorem ipsum dolor sit amet consectetur adipiscing elit sed do eiusmod</div></div>
    <div class="dot" style="left:162px;top:104px;width:8px;height:8px;border:.6px solid #222;color:#222"><svg class="i" style="width:4.5px;height:4.5px"><use href="#chat"/></svg></div>
    <div class="a" style="left:174px;top:104px;width:50px"><div class="h" style="font-size:2px">Lorem ipsum dolor</div><div class="t" style="font-size:1.8px;line-height:2.4px">Lorem ipsum dolor sit amet consectetur adipiscing elit sed do eiusmod</div></div>
    <div class="dot" style="left:98px;top:127px;width:8px;height:8px;border:.6px solid #222;color:#222"><svg class="i" style="width:4.5px;height:4.5px"><use href="#phone"/></svg></div>
    <div class="a" style="left:110px;top:127px;width:50px"><div class="h" style="font-size:2px">Lorem ipsum dolor</div><div class="t" style="font-size:1.8px;line-height:2.4px">Lorem ipsum dolor sit amet consectetur adipiscing elit sed do eiusmod</div></div>
    <div class="dot" style="left:162px;top:127px;width:8px;height:8px;border:.6px solid #222;color:#222"><svg class="i" style="width:4.5px;height:4.5px"><use href="#bell"/></svg></div>
    <div class="a" style="left:174px;top:127px;width:50px"><div class="h" style="font-size:2px">Lorem ipsum dolor</div><div class="t" style="font-size:1.8px;line-height:2.4px">Lorem ipsum dolor sit amet consectetur adipiscing elit sed do eiusmod</div></div>
  </section>

  <!-- 23 Photo with list -->
  <section class="slide">
    <div class="photo ph-player" role="img" aria-label="Photo of a player wearing a headset" style="left:0;top:0;width:119px;height:173px;background:linear-gradient(160deg,#1a2238,#0d1220 55%,#2a1a18)"></div>
    <div class="a" style="left:12px;top:86px;width:100px;font-size:2.4px;line-height:3.1px;color:#e4e4e4">Iste natus error sit voluptatem accusantium doloremque laudantium, totam rem aperiam, eaque ipsa quae ab illo inventore veritatis et quasi architecto beatae vitae dicta sunt explicabo. Nemo enim ipsam voluptatem quia voluptas sit aspernatur aut odit aut fugit, sed quia consequuntur magni dolores eos qui ratione voluptatem sequi nesciunt. Neque porro quisquam est, qui dolorem ipsum quia dolor sit amet, consectetur, adipisci velit, commodi consequatur.</div>
    <div class="dot" style="left:137px;top:34px;width:11px;height:11px;background:#1b1b1b;color:#fff"><svg class="i" style="width:6px;height:6px"><use href="#mail"/></svg></div>
    <div class="a" style="left:153px;top:34px;width:66px"><div class="h" style="font-size:2.4px">Lorem ipsum dolor</div><div class="t" style="font-size:2.1px;line-height:2.8px">Lorem ipsum dolor sit amet, consectetur adipiscing elit, sed do eiusmod tempor incididunt ut labore et dolore</div></div>
    <div class="dot" style="left:137px;top:65px;width:11px;height:11px;background:#1b1b1b;color:#fff"><svg class="i" style="width:6px;height:6px"><use href="#chat"/></svg></div>
    <div class="a" style="left:153px;top:65px;width:66px"><div class="h" style="font-size:2.4px">Lorem ipsum dolor</div><div class="t" style="font-size:2.1px;line-height:2.8px">Lorem ipsum dolor sit amet, consectetur adipiscing elit, sed do eiusmod tempor incididunt ut labore et dolore</div></div>
    <div class="dot" style="left:137px;top:95px;width:11px;height:11px;background:#1b1b1b;color:#fff"><svg class="i" style="width:6px;height:6px"><use href="#phone"/></svg></div>
    <div class="a" style="left:153px;top:95px;width:66px"><div class="h" style="font-size:2.4px">Lorem ipsum dolor</div><div class="t" style="font-size:2.1px;line-height:2.8px">Lorem ipsum dolor sit amet, consectetur adipiscing elit, sed do eiusmod tempor incididunt ut labore et dolore</div></div>
    <div class="dot" style="left:137px;top:126px;width:11px;height:11px;background:#1b1b1b;color:#fff"><svg class="i" style="width:6px;height:6px"><use href="#bell"/></svg></div>
    <div class="a" style="left:153px;top:126px;width:66px"><div class="h" style="font-size:2.4px">Lorem ipsum dolor</div><div class="t" style="font-size:2.1px;line-height:2.8px">Lorem ipsum dolor sit amet, consectetur adipiscing elit, sed do eiusmod tempor incididunt ut labore et dolore</div></div>
  </section>

  <!-- 24 Thank you -->
  <section class="slide">
    <div class="photo" role="img" aria-label="Photo of a dimly lit esports arena" style="left:0;top:0;width:119px;height:173px;background:linear-gradient(150deg,#3a1518,#141414 45%,#0c0c0c 70%,#1e1212)"></div>
    <div class="a" style="left:13px;top:97px;font-size:13.5px;font-weight:400;color:#fff;letter-spacing:.3px">THANK YOU</div>
    <div class="a" style="left:22px;top:116px;font-size:5px;color:#ccc">For Your Precious Time</div>
    <div class="a" style="left:134px;top:102px;font-size:4.8px;font-weight:700;color:#222">CONTACT INFO</div>
    <div class="a" style="left:135px;top:114px;display:flex;align-items:center;gap:3px;font-size:3.6px;color:#333"><svg class="i" style="width:5px;height:5px"><use href="#call"/></svg>+1 555 014 2290</div>
    <div class="a" style="left:135px;top:125px;display:flex;align-items:center;gap:3px;font-size:3.6px;color:#333"><svg class="i" style="width:5px;height:5px"><use href="#mail"/></svg>hello@questline.io</div>
    <div class="a" style="left:135px;top:136px;display:flex;align-items:center;gap:3px;font-size:3.6px;color:#333"><svg class="i" style="width:5px;height:5px"><use href="#globe"/></svg>www.questline.io</div>
  </section>

</main>
</body>
</html>
```